PROFESSIONAL MODERN REDESIGN OF CURRENT WEBSITE USING ALL SAME CONTENT

I need to redesign existing website using all existing exact content. Please do not leave anything missing. Use all content.

www.brightpathpromotionsgroup.biz

Target Market(s)

Small business owners, business to business, B2B

Industry/Entity Type

Direct Marketing

Number of Pages Required

5+ page

Colors

Designer to choose colors to be used in the design.

Requirements
Must have
• Must use exact same content as www.brightpathpromotionsgroup.biz
Nice to have
• I'd like this to be an easy to read professionally designed website with all modern elements...
Should not have
• Open

```html
<!DOCTYPE html>
<html lang="en">
<head>
<meta charset="utf-8">
<title>Testimonials – BrightPath Promotions</title>
<link href="https://fonts.googleapis.com/css2?family=Montserrat:ital,wght@0,300;0,400;0,500;0,600;0,700;1,400&display=swap" rel="stylesheet">
<style>
:root{
  --ink:#17212b;
  --navy:#243a52;
  --blue:#0a94ef;
  --brand:#1a86d6;
  --text:#4a4a4a;
  --muted:#666;
  --line:#e4e8ee;
  --quote:#dbe4ee;
  --white:#fff;
}
*{box-sizing:border-box;margin:0;padding:0}
html,body{width:1200px;height:3576px;overflow:hidden}
body{font-family:'Montserrat',sans-serif;color:var(--text);background:var(--white)}
a{color:inherit;text-decoration:none}

.topbar{height:28px;background:var(--ink);color:var(--white);font-size:10.5px;display:flex;align-items:center;justify-content:space-between;padding:0 109px 0 122px}
.topbar .account{font-weight:700;letter-spacing:1.5px}
.topbar .account span{margin:0 12px}

.site-header{height:116px;text-align:center}
.brand{display:inline-flex;align-items:center;gap:10px;margin-top:22px;font-weight:700;font-size:24px;color:var(--brand);letter-spacing:.5px}
.brand .mark{width:18px;height:18px;background:var(--brand)}
.main-nav{display:flex;justify-content:center;gap:32px;margin-top:22px;font-size:11px;font-weight:500;color:#333}
.main-nav .current{color:var(--blue)}

.hero{height:350px;background:linear-gradient(115deg,#3f73c4 0%,#2b5aa8 35%,#102a55 50%,#3a78cf 62%,#5d95e0 80%,#15305e 100%);display:flex;align-items:center;justify-content:center}
.hero h1{color:var(--white);font-weight:300;font-size:50px;letter-spacing:5px;margin-top:-14px}

.testimonials{height:2409px;position:relative}
.filters{position:absolute;top:77px;left:82px;display:flex;gap:32px}
.filters a{width:324px;height:63px;background:var(--blue);color:var(--white);display:flex;align-items:center;justify-content:center;font-weight:500;font-size:18px;letter-spacing:1.8px;border-radius:2px}

.card{position:absolute;left:69px;width:1064px;border:1.5px solid var(--line);border-radius:28px;padding:44px 100px 0 113px}
.card .q-open,.card .q-close{position:absolute;font-family:Georgia,serif;font-weight:700;font-size:78px;line-height:1;color:var(--quote)}
.card .q-open{left:31px;top:22px}
.card .q-close{right:30px;bottom:-14px}
.card p{font-size:18px;line-height:31px;color:var(--text)}
.author{display:flex;align-items:center;margin-top:22px;margin-left:-6px}
.badge{width:60px;height:60px;border-radius:50%;background:var(--blue);margin-right:18px}
.author strong{display:block;color:var(--blue);font-weight:600;font-size:18px}
.author em{font-size:18px;color:var(--muted)}

.site-footer{height:588px;background:var(--navy);color:var(--white);position:relative}
.fcol{position:absolute;top:76px}
.fcol h4{color:var(--blue);font-weight:500;font-size:12.5px;letter-spacing:3px;margin-bottom:18px}
.fcol .f-brand{display:flex;align-items:center;gap:8px;font-weight:700;font-size:30px;color:var(--brand);margin-bottom:30px}
.fcol .f-brand i{width:14px;height:14px;background:var(--brand)}
.fcol p{font-size:11px;font-weight:600;line-height:21px;margin-bottom:30px}
.fcol ul{list-style:none;font-size:11px;font-weight:600}
.fcol li{height:28.7px}
.col-contact{left:230px;width:230px}
.col-links{left:555px}
.col-social{left:858px}
.copyright{height:83px;background:var(--ink);color:var(--blue);font-size:11px;display:flex;align-items:center;justify-content:center}
</style>
</head>
<body>
<div class="topbar">
  <div>USA Office : 555-210-4471 &nbsp;|&nbsp; International : 1-800-555-0142</div>
  <div class="account"><a href="#">LOGIN</a><span>|</span><a href="#">SIGNUP</a></div>
</div>

<header class="site-header">
  <a class="brand" href="#"><span class="mark"></span>BrightPath Promotions</a>
  <nav class="main-nav">
    <a href="#">HOME</a><a href="#">OUR INCENTIVES</a><a href="#">SAMPLES</a><a href="#">AFFILIATES</a><a href="#" class="current">TESTIMONIALS</a><a href="#">FAQ</a><a href="#">CONTACT</a>
  </nav>
</header>

<section class="hero" role="img" aria-label="Photo of blue glass skyscraper facades seen from below">
  <h1>TESTIMONIALS</h1>
</section>

<main class="testimonials">
  <div class="filters">
    <a href="#">BPP USER TESTIMONIALS</a>
    <a href="#">DINING TESTIMONIALS</a>
    <a href="#">TRAVELER TESTIMONIALS</a>
  </div>

  <article class="card" style="top:208px;height:249px">
    <span class="q-open">“</span><span class="q-close">”</span>
    <p>Travel agency was prompt in all of their responses. You can get a good deal! I was very specific in the dates and places I needed, so I completely understood why I needed to pay a little more. Thank you for your timely responses!</p>
    <div class="author"><span class="badge"></span><div><strong>Marla T.</strong><em>Appleton, WI</em></div></div>
  </article>

  <article class="card" style="top:509px;height:276px">
    <span class="q-open">“</span><span class="q-close">”</span>
    <p>As this was the first time I have ever completed one of these, I was a bit nervous...but the travel agency made our booking painless. They made sure I had the best deal for what I wanted to experience. I will certainly choose to make this a choice of traveling as we look to see more of the world!</p>
    <div class="author"><span class="badge"></span><div><strong>Dan K.</strong><em>San Antonio, TX</em></div></div>
  </article>

  <article class="card" style="top:838px;height:276px">
    <span class="q-open">“</span><span class="q-close">”</span>
    <p>I worked with the travel agency and they were very patient with me as I narrowed down where myself and another friend wanted to travel to. I gave them destinations and in return they gave me prompt responses on what was available and in our budget. Don't hesitate to work with this travel agency.....because I won't!</p>
    <div class="author"><span class="badge"></span><div><strong>Owen B.</strong><em>Duluth, GA</em></div></div>
  </article>

  <article class="card" style="top:1194px;height:195px">
    <span class="q-open">“</span><span class="q-close">”</span>
    <p>The travel agency did an excellent job booking my trip to Nashville.</p>
    <div class="author"><span class="badge"></span><div><strong>Victor L.</strong><em>North Las Vegas, NV</em></div></div>
  </article>

  <article class="card" style="top:1472px;height:249px">
    <span class="q-open">“</span><span class="q-close">”</span>
    <p>Wonderful! It was just like being in Rome, but only with great shows to enjoy. The rooms of the Grand Vista and service were excellent. Going through the travel agency was simple and easy on the purse strings.</p>
    <div class="author"><span class="badge"></span><div><strong>Neil S.</strong><em>Flagstaff, AZ</em></div></div>
  </article>

  <article class="card" style="top:1796px;height:222px">
    <span class="q-open">“</span><span class="q-close">”</span>
    <p>The certificates have been tremendous! We have been able to enjoy new restaurants each month.</p>
    <div class="author"><span class="badge"></span><div><strong>Carla M.</strong><em>Denver, CO</em></div></div>
  </article>

  <article class="card" style="top:2086px;height:195px">
    <span class="q-open">“</span><span class="q-close">”</span>
    <p>Great way to check out new dining experiences.</p>
    <div class="author"><span class="badge"></span><div><strong>Tom F.</strong><em>Studio City, CA</em></div></div>
  </article>
</main>

<footer>
  <div class="site-footer">
    <div class="fcol col-contact">
      <div class="f-brand"><i></i>BPP</div>
      <h4>CONTACT DETAILS</h4>
      <p>BrightPath Promotions Group, Inc.<br>1470 Harborview Drive<br>Coastal City CA 90000</p>
      <h4>HOURS</h4>
      <p>Monday - Friday: 8:00AM - 5:00PM PST-<br>Saturday - Sunday: CLOSED</p>
    </div>
    <div class="fcol col-links">
      <h4>QUICKLINKS</h4>
      <ul>
        <li>Home</li><li>Our Incentives</li><li>Samples</li><li>Affiliate</li><li>Testimonials</li><li>FAQ</li><li>Contact Us</li><li>Terms &amp; Conditions</li><li>Privacy Policy</li><li>Hoteliers</li><li>BPP PDF Flyer</li><li>BPP PDF Brochure</li><li>BPP Certificates List</li><li>How To Use BPP Certificates</li><li>Free Viseo Ad Mock Up for Marketing</li>
      </ul>
    </div>
    <div class="fcol col-social">
      <h4>SOCIAL</h4>
      <ul><li>Chatterly</li><li>ClipStream</li><li>WorkLink</li><li>SnapGrid</li></ul>
    </div>
  </div>
  <div class="copyright">Copyright 2005-2020 BrightPath Promotions Group, Inc. All Rights Reserved.</div>
</footer>
</body>
</html>
```